Face cream packaging | Cosmetic start-up

This project is about creating design proposals for two different types of packaging. Once to a cream jar made of glass and once to a jar made of plastic.
Three different designs must be created for each type of jar. Later, the different packaging will be used as customization options in an online store for cosmetics.

- The packaging variant made of glass should have color gradients. Three different shades are to be chosen. (Preferably with the primary colors red, blue and green). Note: The designer can create other proposals at will if he has better ideas. The logo must be included in some form. (Link to manufacturer description: https://catalogue.vorelpackwerk.com/en/portals/vorelpackwerk/assets/48302915/lio-50-ml/)

- With the plastic type of packaging, the designer has a lot of freedom to design. The only requirement is that the design must be artistic. It doesn't matter whether abstract patterns, geometric figures, mandalas or just a basic color is chosen. The main thing is that the packaging inspires. The logo must be included in some form. (Link to manufacturer description: https://catalogue.vorelpackwerk.com/en/portals/vorelpackwerk/assets/48302922/tova-50-ml/)

Thank you in advance for your work and best regards
Ubel

Target Market(s)

Young people with an affinity for social media and the web. Focus is on the female clientele.

Industry/Entity Type

Cosmetics

Font styles to use
Script

Colors
eea4c8
f59195
85cae6
cadf82

Requirements
Must have
• The logo must be included in some form. (PNG-File attached)
Nice to have
• Other types of packaging (can shape, packaging material)

```html
<!DOCTYPE html>
<html lang="en">
<head>
<meta charset="utf-8">
<title>Noa Bloom – Face Cream Labels</title>
<link href="https://fonts.googleapis.com/css2?family=Lato:wght@300;400;700&display=swap" rel="stylesheet">
<style>
  :root {
    --page-bg: #ffffff;
    --ink: #111111;
    --frame: #ffffff;
    --green-top: #3fe6c0;
    --green-mid: #9aec8a;
    --green-bottom: #d6ee6a;
    --teal-top: #a8ece0;
    --teal-mid: #5fc4c8;
    --teal-bottom: #3a63a8;
    --violet-top: #6a3cf0;
    --violet-mid: #b43ad2;
    --violet-bottom: #f0506e;
    --decor-tint: rgba(255, 255, 255, 0.28);
  }

  * { box-sizing: border-box; margin: 0; padding: 0; }

  html, body {
    width: 1200px;
    height: 675px;
    overflow: hidden;
    background: var(--page-bg);
  }

  .label-set {
    position: relative;
    width: 1200px;
    height: 675px;
    display: flex;
    justify-content: center;
    align-items: center;
    gap: 40px;
  }

  .jar-label {
    position: relative;
    width: 340px;
    height: 230px;
    overflow: hidden;
    font-family: 'Lato', sans-serif;
    color: var(--ink);
  }

  .jar-label--green {
    background: linear-gradient(180deg, var(--green-top) 0%, var(--green-mid) 50%, var(--green-bottom) 100%);
  }
  .jar-label--teal {
    background: linear-gradient(180deg, var(--teal-top) 0%, var(--teal-mid) 55%, var(--teal-bottom) 100%);
  }
  .jar-label--violet {
    background: linear-gradient(180deg, var(--violet-top) 0%, var(--violet-mid) 50%, var(--violet-bottom) 100%);
  }

  .decor {
    position: absolute;
    background: var(--decor-tint);
    border-radius: 50%;
  }

  .decor--ring {
    left: 22px; top: -10px;
    width: 220px; height: 250px;
    background: transparent;
    border: 10px solid var(--decor-tint);
  }
  .decor--leaves-left  { left: -20px; top: -10px; width: 90px; height: 250px; }
  .decor--leaves-right { right: -20px; top: 0; width: 100px; height: 90px; }
  .decor--leaves-corner { right: -10px; bottom: -10px; width: 110px; height: 80px; }
  .decor--branch-left  { left: -20px; top: 40px; width: 110px; height: 170px; }
  .decor--branch-right { right: -20px; top: -10px; width: 90px; height: 100px; }
  .decor--branch-low   { right: -10px; bottom: -20px; width: 110px; height: 110px; }

  .brand {
    position: absolute;
    left: 0; right: 0;
    top: 40px;
    text-align: center;
  }

  .brand__name {
    font-weight: 300;
    font-size: 40px;
    letter-spacing: 1px;
    line-height: 1;
  }

  .brand__rule {
    display: block;
    width: 170px;
    height: 1px;
    margin: 18px auto 0 auto;
    background: var(--frame);
    transform: translateX(30px);
  }

  .product-info {
    position: absolute;
    left: 0; right: 0;
    top: 136px;
    text-align: center;
  }

  .product-info__line {
    display: inline-block;
    font-weight: 400;
    font-size: 14px;
    padding: 2px 10px;
    border: 1px solid var(--frame);
  }

  .product-info__name {
    margin-top: 8px;
    font-size: 8px;
    font-weight: 400;
  }

  .product-info__volume {
    margin-top: 9px;
    font-size: 8px;
    font-weight: 400;
  }
</style>
</head>
<body>
  <main class="label-set">

    <section class="jar-label jar-label--green">
      <div class="decor decor--ring" role="img" aria-label="White brush-stroke circle decoration"></div>
      <div class="brand">
        <p class="brand__name">Noa Bloom</p>
        <span class="brand__rule"></span>
      </div>
      <div class="product-info">
        <p class="product-info__line">Natural Skincare</p>
        <p class="product-info__name">Zinc Reparing Facial Cream</p>
        <p class="product-info__volume">50ml</p>
      </div>
    </section>

    <section class="jar-label jar-label--teal">
      <div class="decor decor--leaves-left" role="img" aria-label="White line-drawn leaves climbing the left edge"></div>
      <div class="decor decor--leaves-right" role="img" aria-label="White line-drawn leaves at the top right"></div>
      <div class="decor decor--leaves-corner" role="img" aria-label="White line-drawn leaves at the bottom right"></div>
      <div class="brand">
        <p class="brand__name">Noa Bloom</p>
        <span class="brand__rule"></span>
      </div>
      <div class="product-info">
        <p class="product-info__line">Natural Skincare</p>
        <p class="product-info__name">Zinc Reparing Facial Cream</p>
        <p class="product-info__volume">50ml</p>
      </div>
    </section>

    <section class="jar-label jar-label--violet">
      <div class="decor decor--branch-left" role="img" aria-label="White line-drawn fern branch on the left"></div>
      <div class="decor decor--branch-right" role="img" aria-label="White line-drawn leaf sprig at the top right"></div>
      <div class="decor decor--branch-low" role="img" aria-label="White line-drawn fern branch at the bottom right"></div>
      <div class="brand">
        <p class="brand__name">Noa Bloom</p>
        <span class="brand__rule"></span>
      </div>
      <div class="product-info">
        <p class="product-info__line">Natural Skincare</p>
        <p class="product-info__name">Zinc Reparing Facial Cream</p>
        <p class="product-info__volume">50ml</p>
      </div>
    </section>

  </main>
</body>
</html>
```